Coffee roastery and coffee shop needs a packaging design

We need a packaging design for an our company we sell coffee beans for coffee shops . and we have a coffee shop . our company name is (BRAMBLE ROASTERY) we are based in UAE. We want a cup design for cold coffee and hot and coffee bag design and paper bag design. I uploaded our logo design.

```html
<!DOCTYPE html>
<html lang="en">
<head>
<meta charset="utf-8">
<title>Bramble Roastery – Coffee Bag Label</title>
<link href="https://fonts.googleapis.com/css2?family=Michroma&family=Raleway:wght@300;400&display=swap" rel="stylesheet">
<style>
  :root {
    --canvas: #ffffff;
    --band-yellow: #f6e08f;
    --panel-light: #ffffff;
    --panel-grey: #e6e7e8;
    --ink: #333333;
    --ink-soft: #666666;
    --berry: #a3262b;
    --leaf-line: #b9b07a;
    --bean-brown: #8a6a55;
    --bean-peach: #f2c49a;
  }
  * { margin: 0; padding: 0; box-sizing: border-box; }
  html, body {
    width: 1200px; height: 1200px; overflow: hidden;
    background: var(--canvas);
  }
  .label {
    position: absolute; left: 134px; top: 55px;
    width: 932px; height: 1089px;
    background: linear-gradient(225deg, var(--panel-grey) 0%, #eeeeef 45%, var(--panel-light) 100%);
    overflow: hidden;
  }
  .side-band {
    position: absolute; left: 0; top: 0;
    width: 217px; height: 100%;
    background: var(--band-yellow);
  }
  .side-band .brand-name {
    position: absolute; left: 0; right: 0; top: 700px;
    text-align: center;
    font-family: "Michroma", sans-serif;
    font-size: 11px; letter-spacing: 3px; line-height: 1.6;
    color: var(--ink);
  }
  .berry-branch {
    position: absolute; left: 216px; top: 0;
    width: 308px; height: 216px;
    background: radial-gradient(ellipse at 55% 55%, rgba(163,38,43,0.35) 0%, rgba(185,176,122,0.25) 45%, rgba(255,255,255,0) 75%);
  }
  .main-brand {
    position: absolute; left: 400px; width: 348px; top: 300px;
    text-align: center; color: var(--ink);
  }
  .main-brand .brand-dot {
    width: 110px; height: 110px; margin: 0 auto 34px;
    border: 5px solid var(--ink); border-radius: 50%;
  }
  .main-brand .brand-name {
    font-family: "Michroma", sans-serif;
    font-size: 20px; letter-spacing: 6px; line-height: 1.5;
  }
  .falling-beans {
    position: absolute; left: 447px; top: 441px;
    width: 231px; height: 341px;
    background: radial-gradient(ellipse at 50% 40%, rgba(138,106,85,0.28) 0%, rgba(242,196,154,0.22) 45%, rgba(255,255,255,0) 72%);
  }
  .arabica-badge {
    position: absolute; left: 342px; top: 718px;
    width: 66px; height: 66px;
    border: 4px solid var(--ink); border-radius: 50%;
  }
  .origin-note {
    position: absolute; left: 295px; width: 160px; top: 786px;
    text-align: center;
    font-family: "Raleway", sans-serif; font-size: 9px; color: var(--ink-soft);
  }
  .product-type {
    position: absolute; left: 431px; width: 300px; top: 814px;
    text-align: center; color: var(--ink);
  }
  .product-type .kicker {
    font-family: "Raleway", sans-serif; font-weight: 300;
    font-size: 17px; letter-spacing: 0.5px;
  }
  .product-type .product {
    font-family: "Michroma", sans-serif;
    font-size: 34px; letter-spacing: 6px; line-height: 1.1;
  }
  .brew-methods {
    position: absolute; left: 467px; top: 888px;
    display: flex; gap: 0;
  }
  .brew-method {
    width: 62px; text-align: center;
    font-family: "Raleway", sans-serif; font-size: 8px; color: var(--ink-soft);
  }
  .brew-method svg { display: block; margin: 0 auto 6px; height: 26px; width: 30px; }
  .net-weight {
    position: absolute; left: 491px; width: 200px; top: 976px;
    text-align: center;
    font-family: "Michroma", sans-serif; font-size: 16px; letter-spacing: 3px;
    color: var(--ink);
  }
  .leaf-drawing {
    position: absolute; left: 760px; top: 851px;
    width: 172px; height: 238px;
    background: linear-gradient(200deg, rgba(185,176,122,0) 10%, rgba(185,176,122,0.28) 55%, rgba(185,176,122,0) 95%);
  }
</style>
</head>
<body>
  <div class="label">
    <div class="side-band">
      <p class="brand-name">BRAMBLE<br>ROASTERY</p>
    </div>

    <div class="berry-branch" role="img" aria-label="Line drawing of a coffee branch with red coffee cherries"></div>

    <div class="main-brand">
      <div class="brand-dot"></div>
      <p class="brand-name">BRAMBLE<br>ROASTERY</p>
    </div>

    <div class="falling-beans" role="img" aria-label="Illustration of scattered coffee beans in red, green, brown, peach and yellow"></div>

    <div class="arabica-badge"></div>
    <p class="origin-note">PRODUCED IN THE UAE</p>

    <div class="product-type">
      <p class="kicker">ROASTED AND GROUND</p>
      <p class="product">COFFEE</p>
    </div>

    <div class="brew-methods">
      <div class="brew-method">
        <svg viewBox="0 0 30 26" fill="none" stroke="#333" stroke-width="1.6">
          <path d="M4 6 H26 L17 18 H13 Z"/><path d="M10 22 H20"/>
        </svg>FILTER
      </div>
      <div class="brew-method">
        <svg viewBox="0 0 30 26" fill="none" stroke="#333" stroke-width="1.6">
          <circle cx="8" cy="8" r="4"/><path d="M11 10 L27 20" stroke-width="3.5"/>
        </svg>ESPRESSO
      </div>
      <div class="brew-method">
        <svg viewBox="0 0 30 26" fill="none" stroke="#333" stroke-width="1.6">
          <path d="M15 1 V5"/><path d="M10 5 H20"/><rect x="9" y="7" width="12" height="16"/><path d="M21 10 H24 V19 H21"/>
        </svg>PLUNGER
      </div>
      <div class="brew-method">
        <svg viewBox="0 0 30 26" fill="#333">
          <ellipse cx="11" cy="8" rx="4" ry="5.5"/><ellipse cx="20" cy="11" rx="4" ry="5.5"/><ellipse cx="12" cy="19" rx="4" ry="5.5"/>
        </svg>BEANS
      </div>
    </div>

    <p class="net-weight">400G</p>

    <div class="leaf-drawing" role="img" aria-label="Line drawing of a large leaf"></div>
  </div>
</body>
</html>
```